Pebble Ledger WEB application

We need a small webdesign for a WEB-Application. Functionality will be provided by our developers. All we need are templates with HTML5, CSS and Java functionality for the "animated" parts. As well as some images and logos .
See attached Powerpoint. Please ignore last slide.
Design should be state of the art material design as know from Quorvix or Zelpad latest OS versions
In the end will be fluid design (fitting automatically to actual screen size) but template should base on 540 x 960

Target Market(s)

UK Mobile Market

Number of Pages Required

5+ page

Font styles to use
Sans Serif

Requirements
Must have
• next to requierements in Powerpoint we need animations as stated in PP (progress animation).
Nice to have
• All textfiles should be in a XML file to be easily translated to other languages.Can be done by our developers as well

```html
<!DOCTYPE html>
<html lang="en">
<head>
<meta charset="utf-8">
<title>Pebble Ledger</title>
<link rel="stylesheet" href="https://fonts.googleapis.com/css2?family=Open+Sans:wght@400;600;700&display=swap">
<style>
  :root {
    --ink: #1d1d1d;
    --muted: #3a3a3a;
    --paper: #ffffff;
    --panel-top: #f2f2f2;
    --panel-bottom: #e4e4e4;
    --rule: #cfcfcf;
    --header-top: #3a3a3a;
    --header-bottom: #050505;
    --alert: #e0262b;
    --green: #55b94a;
    --green-light: #7fd067;
    --green-dark: #3f9c36;
    --tab-bg: #141414;
    --tab-rule: #3a3a3a;
  }
  * { box-sizing: border-box; margin: 0; padding: 0; }
  html, body { width: 675px; height: 1200px; overflow: hidden; background: var(--paper); }
  body { font-family: "Open Sans", Arial, sans-serif; color: var(--ink); }
  .screen { position: relative; width: 675px; height: 1200px; background: linear-gradient(var(--panel-top), var(--panel-bottom)); }

  .status-bar { position: absolute; top: 0; left: 0; width: 100%; height: 34px; background: var(--paper);
    display: flex; align-items: center; justify-content: space-between; padding: 0 12px; font-size: 21px; font-weight: 600; }
  .status-bar .clock { position: absolute; left: 0; right: 0; text-align: center; }
  .status-left, .status-right { display: flex; align-items: center; gap: 6px; position: relative; z-index: 1; }

  .app-header { position: absolute; top: 34px; left: 0; width: 100%; height: 124px;
    background: linear-gradient(var(--header-top), var(--header-bottom));
    color: var(--paper); display: flex; align-items: center; justify-content: center; font-size: 48px; font-weight: 400; }

  .notice { position: absolute; top: 158px; left: 0; width: 100%; height: 162px; text-align: center; border-bottom: 2px solid var(--rule); }
  .notice-title { margin-top: 52px; font-size: 36px; letter-spacing: 2px; color: var(--ink); font-weight: 400; }
  .notice-title .alert { color: var(--alert); font-weight: 700; }
  .notice-text { margin-top: 2px; font-size: 24px; color: var(--muted); }

  .battery-visual { position: absolute; top: 345px; left: 170px; width: 335px; height: 195px; border-radius: 12px;
    background: linear-gradient(90deg, #f4d6d6 0%, #eeeeee 25%, #e4f2df 100%); }

  .savings { position: absolute; top: 652px; left: 0; width: 100%; height: 110px; border-top: 2px solid var(--rule);
    text-align: center; font-size: 40px; color: var(--muted); padding-top: 34px; }
  .savings .figure { color: var(--alert); }

  .cta { position: absolute; top: 783px; left: 74px; width: 545px; height: 86px; border-radius: 6px;
    background: linear-gradient(var(--green-light), var(--green-dark)); border: 1px solid var(--green-dark);
    color: var(--paper); font-size: 36px; display: flex; align-items: center; justify-content: center; font-weight: 400; }

  .pitch { position: absolute; top: 908px; left: 0; width: 100%; height: 126px; border-top: 2px solid var(--rule);
    text-align: center; padding-top: 16px; color: var(--ink); }
  .pitch-line { font-size: 29px; line-height: 46px; }
  .pitch-line .highlight { color: var(--green); font-size: 37px; }
  .pitch-sub { font-size: 31px; line-height: 44px; }

  .tab-bar { position: absolute; bottom: 0; left: 0; width: 100%; height: 166px; background: var(--tab-bg); display: flex; }
  .tab { flex: 1; display: flex; flex-direction: column; align-items: center; justify-content: center; gap: 14px;
    color: var(--paper); font-size: 19px; border-left: 2px solid var(--tab-rule); }
  .tab:first-child { border-left: none; }
  .tab svg { width: 46px; height: 46px; }
</style>
</head>
<body>
<main class="screen">
  <div class="status-bar">
    <div class="status-left">
      <svg width="74" height="14" viewBox="0 0 74 14" aria-hidden="true">
        <circle cx="7" cy="7" r="6" fill="#111"/><circle cx="22" cy="7" r="6" fill="#111"/><circle cx="37" cy="7" r="6" fill="#111"/>
        <circle cx="52" cy="7" r="5.5" fill="none" stroke="#111" stroke-width="1.2"/><circle cx="67" cy="7" r="5.5" fill="none" stroke="#111" stroke-width="1.2"/>
      </svg>
      <svg width="26" height="20" viewBox="0 0 26 20" aria-hidden="true">
        <path d="M2 7a16 16 0 0 1 22 0M6 11a10 10 0 0 1 14 0M10 15a4 4 0 0 1 6 0" fill="none" stroke="#111" stroke-width="2.4" stroke-linecap="round"/>
      </svg>
    </div>
    <span class="clock">4:39 PM</span>
    <div class="status-right">
      <span>100%</span>
      <svg width="44" height="20" viewBox="0 0 44 20" aria-hidden="true">
        <rect x="1" y="1" width="38" height="18" rx="3" fill="none" stroke="#111" stroke-width="2"/>
        <rect x="4" y="4" width="32" height="12" fill="#111"/><rect x="40" y="6" width="3" height="8" fill="#111"/>
      </svg>
    </div>
  </div>

  <header class="app-header">Pebble Ledger</header>

  <section class="notice">
    <h2 class="notice-title">ATTENT<span class="alert">!</span>ON</h2>
    <p class="notice-text">Several Battery rainers found</p>
  </section>

  <div class="battery-visual" role="img" aria-label="Battery illustration with a low red charge level and a red lightning bolt"></div>

  <section class="savings">Your Battery could last <span class="figure">5%</span> longer</section>

  <div class="cta">Start FREE OPTIMIZATION now</div>

  <section class="pitch">
    <p class="pitch-line">World premiere web technology <span class="highlight">100% save</span></p>
    <p class="pitch-sub">No Download Needed,No Access Rights</p>
  </section>

  <nav class="tab-bar">
    <div class="tab">
      <svg viewBox="0 0 24 24" aria-hidden="true"><path d="M5 12a7 7 0 0 1 12-5M19 12a7 7 0 0 1-12 5" fill="none" stroke="#5cc24c" stroke-width="2.2" stroke-linecap="round"/><path d="M17 3v4h-4M7 21v-4h4" fill="none" stroke="#5cc24c" stroke-width="2.2" stroke-linecap="round"/></svg>
      <span>Scan</span>
    </div>
    <div class="tab">
      <svg viewBox="0 0 24 24" aria-hidden="true"><path d="M9 3 5 12h4l-2 9 7-11h-4l2-7z M17 3l-3 7h3l-2 7 5-9h-3l2-5z" fill="#5cc24c"/></svg>
      <span>Optimization</span>
    </div>
    <div class="tab">
      <svg viewBox="0 0 24 24" aria-hidden="true"><rect x="2" y="7" width="18" height="10" rx="1.5" fill="none" stroke="#5cc24c" stroke-width="1.8"/><rect x="20.5" y="10" width="2" height="4" fill="#5cc24c"/></svg>
      <span>Battery Status</span>
    </div>
    <div class="tab">
      <svg viewBox="0 0 24 24" aria-hidden="true"><circle cx="12" cy="12" r="7" fill="#5cc24c"/><path d="M12 2v4M12 18v4M2 12h4M18 12h4M5 5l3 3M16 16l3 3M5 19l3-3M16 8l3-3" stroke="#5cc24c" stroke-width="2.6" stroke-linecap="round"/><circle cx="12" cy="12" r="2.5" fill="#141414"/></svg>
      <span>Special Offer</span>
    </div>
    <div class="tab">
      <svg viewBox="0 0 24 24" aria-hidden="true"><circle cx="12" cy="12" r="6.5" fill="#5cc24c"/><path d="M12 3v3M12 18v3M3 12h3M18 12h3M5.6 5.6l2.2 2.2M16.2 16.2l2.2 2.2M5.6 18.4l2.2-2.2M16.2 7.8l2.2-2.2" stroke="#5cc24c" stroke-width="3" stroke-linecap="round"/><circle cx="12" cy="12" r="2.5" fill="#141414"/></svg>
      <span>Setting</span>
    </div>
  </nav>
</main>
</body>
</html>
```